Business Card Design Project

Hi Designers, this project is currently on hold until the Logo is completed:
Please submit to the Logo project here:
http://jobs.pixelmarket.example/job.aspx?id=371905

Once logo is completed, it will be attached to this project for you to create business cards with show logo, company name and address

Maren T K Ashdown

Corwin's Meadow Pine Flock Co.
Hazelmere
Upper Brackwell
North Devon EX21 4TN

Tel: 01809 351846
Mobile: 07912 463078
email: maren@meadow-pine-flock.example
Updates

Project Deadline Extended
Reason: Sorry everyone, we have had a sick ewe and I am now behind with this one and need to extend the deadline. Best wishes Maren

The designer who wins the logo brief will be asked to design the business card. Many thanks Maren

Project Deadline Extended
Reason: Sorry everyone, just a chaotic time of year with animals. Need to extend the deadline again..... as I just haven't had enough time to take a good look.... Thank you for your understanding. Maren

Project Deadline Extended
Reason: Sorry everyone It is our busiest time of year with animals and just no time to spend going through such great designs. I will have to extend the deadline again and hopefully have some news very soon. Wishing you all a very happy Christmas and a happy and healthy new year. Maren & Corwin

Target Market(s)

High end market
Boutique restaurants for meat (it's not commercial lamb it's a slow matured quality meat more like venison/beef) expensive - specialized market

High End shoot clothing / wool / sheepskin rugs
Quality products

Industry/Entity Type

Business

Requirements
Must have
• based on the logo - (which Pixel Market has just been asked to do)
possibly based on a simplified picture of a Hebridean Ram (shows it's a Hebridean by it's horns as opposed to other black sheep!!)

```html
<!DOCTYPE html>
<html lang="en">
<head>
<meta charset="utf-8">
<title>Corwin's Meadow Pine Flock Co. — Business Card</title>
<link href="https://fonts.googleapis.com/css2?family=Cinzel:wght@400;700&display=swap" rel="stylesheet">
<style>
  :root {
    --backdrop: #e6e6e6;
    --card-white: #fbfbfa;
    --card-dark: #2a2f2f;
    --ink: #1f2323;
    --ring: #3a3f3f;
    --on-dark: #f2f2f2;
  }
  * { box-sizing: border-box; margin: 0; padding: 0; }
  html, body { width: 1200px; height: 720px; overflow: hidden; }
  body {
    background: var(--backdrop);
    font-family: "Cinzel", serif;
    color: var(--ink);
    position: relative;
  }
  .card {
    position: absolute;
    top: 211px;
    width: 520px;
    height: 297px;
    overflow: hidden;
  }
  .card--front { left: 50px; background: var(--card-white); }
  .card--back { left: 630px; background: var(--card-dark); color: var(--on-dark); }

  .front-ring { position: absolute; left: 0; top: 0; }

  .brand {
    position: absolute;
    left: 12px;
    top: 22px;
    display: flex;
    align-items: center;
    gap: 10px;
  }
  .brand__dot {
    width: 60px; height: 60px;
    border: 4px solid var(--ink);
    border-radius: 50%;
    flex: none;
  }
  .brand__name {
    font-size: 17px;
    font-weight: 400;
    line-height: 1.15;
    color: var(--ink);
    width: 190px;
  }

  .person {
    position: absolute;
    left: 232px;
    width: 280px;
    top: 132px;
    text-align: center;
  }
  .person__name { font-size: 15px; font-weight: 700; letter-spacing: 0.3px; }
  .person__role { font-size: 12px; margin-top: 2px; }

  .address {
    position: absolute;
    left: 23px;
    top: 160px;
    font-size: 12px;
    line-height: 15px;
  }
  .contacts {
    position: absolute;
    left: 23px;
    top: 224px;
    list-style: none;
    font-size: 12px;
    line-height: 15px;
  }
  .contacts li { display: flex; align-items: center; gap: 6px; }
  .contacts svg { width: 12px; height: 12px; flex: none; }

  .back-mark {
    position: absolute;
    left: 50%;
    top: 56px;
    transform: translateX(-50%);
    width: 134px; height: 134px;
    border: 8px solid var(--on-dark);
    border-radius: 50%;
  }
  .back-name {
    position: absolute;
    left: 0; right: 0;
    top: 206px;
    text-align: center;
    font-size: 22px;
    font-weight: 400;
    line-height: 1.1;
    letter-spacing: 0.5px;
  }
</style>
</head>
<body>
  <section class="card card--front">
    <svg class="front-ring" width="520" height="297" viewBox="0 0 520 297" aria-hidden="true">
      <circle cx="372" cy="150" r="136" fill="none" stroke="var(--ring)" stroke-width="24"/>
    </svg>

    <div class="brand">
      <span class="brand__dot"></span>
      <span class="brand__name">Corwin's Meadow Pine Flock Co.</span>
    </div>

    <div class="person">
      <p class="person__name">Maren T K Ashdown</p>
      <p class="person__role">Founder &amp; CEO</p>
    </div>

    <address class="address" style="font-style:normal">
      Hazelmere<br>
      Upper Brackwell<br>
      North Devon EX21 4TN
    </address>

    <ul class="contacts">
      <li>
        <svg viewBox="0 0 12 12"><path d="M1 4 Q6 0 11 4 L10 6 L8 5 L8 4 Q6 3 4 4 L4 5 L2 6 Z M3 7 H9 L10 11 H2 Z" fill="var(--ink)"/></svg>
        01809 351846
      </li>
      <li>
        <svg viewBox="0 0 12 12"><rect x="3" y="0.5" width="6" height="11" rx="1" fill="none" stroke="var(--ink)" stroke-width="1.3"/><circle cx="6" cy="9.5" r="0.8" fill="var(--ink)"/></svg>
        07912 463078
      </li>
      <li>
        <svg viewBox="0 0 12 12"><rect x="0.5" y="2" width="11" height="8" fill="var(--ink)"/><path d="M0.5 2 L6 6.5 L11.5 2" fill="none" stroke="var(--card-white)" stroke-width="1"/></svg>
        maren@meadow-pine-flock.example
      </li>
      <li>
        <svg viewBox="0 0 12 12"><rect x="0.8" y="1.5" width="10.4" height="7" fill="none" stroke="var(--ink)" stroke-width="1.3"/><path d="M4 11 H8 M6 8.5 V11" stroke="var(--ink)" stroke-width="1.3"/></svg>
        www.meadow-pine-flock.example
      </li>
    </ul>
  </section>

  <section class="card card--back">
    <span class="back-mark"></span>
    <p class="back-name">Corwin's<br>Meadow Pine Flock Co.</p>
  </section>
</body>
</html>
```